Mentorvale needs a WordPress - Design

I am a personal, team and business coach and help my clients to develop their potential. I mainly work with individuals and teams, but this can also be in the context of a company.
My business is called "Mentorvale"

The main goal of this website is to promote my business and to attire new customers.
I also want to present my concepts and ideas about coaching and how I actually do coaching and consulting. This is also to inform potential customers what coaching actually is and what it's not.
I want to host this website on a hosting-provider and want to be able to add and adapt content on my own. I'm thus looking for a WordPress - design.

Content:

vision
• Why do I do this
• How do I do this
• What am I doing

Coaching
• Career development
• Conflicts
• What is coaching, why coaching
• Conduct of a session and of the whole consultation
Limits of coaching
• Examples of positive effects of coaching

Support concept

Blog about current topics

Left

About me

Contact form

Footer / disclaimer

The following topics are the most important parts of my daily work as a coach with my clients, maybe this helps to get choos a suitable design:
- personality development, analyzing aspects and patterns and showing their influence
- Improve collaboration and cooperation in teams
- Addressing and solving conflicts (private and business)
- Identify and foster motivation, drivers, goals and action patterns
- Define next steps for the further improvement
- Accompany reorientation in professional career
- Discovering and using the strengths of the customers

The major part of my work is direct conversation with the customer, on site or virtually. My job is to support the customer in recognizing his own ideas, goals and possibilities and to define next steps in the desired direction

Target Market(s)

Small businesses and private persons in serch of a professional coach

Industry/Entity Type

Consultant

Number of Pages Required

1 page

Font styles to use
Sans Serif

Requirements
Must have
• - Logo / Name (see attachment)
- Menu, fixed navigation
- content
- blog
- Footer (contact, disclaimer)

- I need a WordPress design suitable for Mobile and Desktop devices.
- I'm looking for a modern, friendly and easy to use web site.
- First page as Long-pager (scrolling), other pages as long-pager or standard
- Decent, friendly colors but still clear, simple
Nice to have
• - Panorama image (image changing on every load of the site)
- Quote (changing on every load of the site)

```html
<!DOCTYPE html>
<html lang="en">
<head>
<meta charset="utf-8">
<title>Mentorvale – Coaching for Individuals, Teams and Business</title>
<link rel="stylesheet" href="https://fonts.googleapis.com/css2?family=Montserrat:wght@400;500;600;700;800&family=Open+Sans:wght@400;600&display=swap">
<style>
:root{
  --blue:#1d6ad8;
  --blue-dark:#0f4fb0;
  --orange:#f5a74b;
  --ink:#1f2430;
  --body:#666b75;
  --muted:#9aa0a8;
  --soft:#f2f3f5;
  --line:#e2e4e8;
  --white:#ffffff;
  --black:#0b0b0c;
}
*{margin:0;padding:0;box-sizing:border-box}
html,body{width:1200px;height:4124px;overflow:hidden}
body{background:var(--white);font-family:"Open Sans",Arial,sans-serif;color:var(--body);font-size:13px;line-height:1.6;position:relative}
h1,h2,h3,h4,.brand,.btn,.nav a{font-family:"Montserrat",Arial,sans-serif;color:var(--ink)}
.btn{display:inline-block;background:var(--orange);color:var(--ink);font-size:12px;font-weight:700;letter-spacing:.5px;padding:12px 30px;text-transform:uppercase;white-space:nowrap}
.btn-blue{background:var(--blue);color:var(--white)}
.ph{position:absolute}

/* header */
.site-header{position:absolute;top:0;left:0;width:1200px;height:130px;z-index:2}
.brand{position:absolute;left:60px;top:22px;display:flex;align-items:center;gap:10px;font-size:20px;font-weight:800;color:var(--blue);letter-spacing:1px}
.brand i{width:34px;height:34px;background:var(--blue);display:block}
.topbar{position:absolute;left:620px;top:12px;font-size:11px;color:var(--body);display:flex;gap:170px;white-space:nowrap}
.nav{position:absolute;left:615px;top:70px;display:flex;gap:28px;align-items:center;white-space:nowrap}
.nav a{font-size:12px;font-weight:600;text-decoration:none}
.social{display:flex;gap:10px;margin-left:14px}
.social span{width:20px;height:20px;border-radius:50%;border:1.5px solid var(--ink);display:block}

/* hero */
.hero{position:absolute;top:0;left:0;width:1200px;height:620px;background:linear-gradient(90deg,#fbfbfc 0%,#f3f4f6 100%)}
.hero-photo{left:460px;top:0;width:740px;height:620px;background:linear-gradient(135deg,#e9ecef 0%,#cdd4dc 45%,#8a96a6 100%)}
.hero-copy{position:absolute;left:80px;top:200px;width:440px}
.hero-copy .eyebrow{font-size:13px;color:var(--ink);font-weight:600}
.hero-copy h1{font-size:46px;line-height:1.1;font-weight:700;margin:8px 0 16px}
.hero-copy p{font-size:14px;color:var(--ink);margin-bottom:26px}
.dots{position:absolute;left:80px;top:650px;display:flex;gap:8px}
.dots span{width:10px;height:10px;border-radius:50%;background:#d4d7dc}
.dots span:first-child{background:var(--orange)}

/* vision */
.vision{position:absolute;left:120px;top:685px;width:960px;height:170px;background:var(--soft);display:flex}
.vision-col{flex:1;padding:26px 40px;text-align:center}
.vision-col+.vision-col{border-left:1px solid var(--line)}
.vision-col h4{font-size:13px;font-weight:700;margin-bottom:10px}
.vision-col p{font-size:11.5px}

/* coaching */
.coaching-bg{position:absolute;left:0;top:875px;width:1200px;height:665px;background:var(--soft)}
.coaching-head{position:absolute;left:150px;top:890px;width:320px}
.coaching-head h2{font-size:25px;line-height:1.2;font-weight:800;text-transform:uppercase}
.coaching-intro{position:absolute;left:490px;top:890px;width:560px;font-size:11.5px}
.cards{position:absolute;left:100px;top:1030px;width:1000px;display:flex;gap:24px}
.card{position:relative;flex:1;height:300px;overflow:hidden}
.card .ph{inset:0}
.card h3{position:absolute;left:22px;bottom:22px;color:var(--white);font-size:19px;font-weight:700;line-height:1.25}
.arrow{position:absolute;top:1165px}
.stats{position:absolute;left:150px;top:1385px;width:900px;display:flex}
.stat{flex:1;display:flex;gap:12px}
.stat b{font-family:"Montserrat",Arial,sans-serif;font-size:32px;color:var(--blue);font-weight:800;line-height:1}
.stat h4{font-size:11px;font-weight:800;text-transform:uppercase}
.stat p{font-size:11px;width:150px}

/* about */
.about-photo{left:130px;top:1600px;width:400px;height:540px;background:linear-gradient(180deg,#eef0f3 0%,#c4ccd6 55%,#3b4656 100%)}
.name-card{position:absolute;left:170px;top:2140px;width:390px;height:110px;background:var(--soft);text-align:center;padding-top:24px}
.name-card h3{font-size:22px;color:var(--blue);font-weight:700}
.name-card p{font-size:14px;color:var(--ink)}
.about{position:absolute;left:630px;top:1600px;width:450px}
.about h2{font-size:24px;font-weight:800;text-transform:uppercase;margin-bottom:16px}
.about p{font-size:11.5px;margin-bottom:12px}
.about h3{font-size:22px;font-weight:700;margin-top:34px}
.form{display:grid;grid-template-columns:1fr 1fr;gap:12px;margin-top:18px;width:440px}
.field{border:1px solid var(--line);height:40px;padding:10px 14px;font-size:11px;color:var(--muted)}
.field.wide{grid-column:1/3}
.field.msg{height:92px}
.form .btn{width:110px;padding:10px 0;text-align:center}

/* support */
.support{position:absolute;left:130px;top:2390px;width:400px}
.support .kicker{font-family:"Montserrat",Arial,sans-serif;font-size:15px;color:var(--blue);font-weight:700}
.support h2{font-size:32px;font-weight:800;margin:2px 0 22px}
.support p{font-size:11.5px;margin-bottom:16px}
.support h3{font-size:20px;font-weight:700;margin:30px 0 8px}
.timeline{position:absolute;left:618px;top:2430px;width:2px;height:420px;background:var(--line)}
.step-dot{position:absolute;left:598px;width:42px;height:42px;border-radius:50%;background:var(--white);border:1px solid var(--line);font-family:"Montserrat",Arial,sans-serif;font-size:12px;font-weight:700;color:var(--ink);display:flex;align-items:center;justify-content:center}
.step-dot.active{background:var(--blue);color:var(--white);border-color:var(--blue)}
.step{position:absolute;left:700px;width:460px;height:148px;background:var(--white);box-shadow:0 4px 18px rgba(0,0,0,.09);padding:22px 28px}
.step h4{font-size:15px;font-weight:700;margin-bottom:8px}
.step p{font-size:11.5px}
.step.active{background:var(--blue)}
.step.active h4,.step.active p{color:var(--white)}

/* blog */
.blog-title{position:absolute;top:2980px;left:0;width:1200px;text-align:center;font-size:36px;font-weight:700}
.posts{position:absolute;left:140px;top:3120px;width:920px;display:flex;gap:40px}
.post{flex:1}
.post .ph{position:relative;height:170px}
.post h4{font-size:16px;font-weight:700;margin-top:20px}
.post p{font-size:11px;color:var(--muted)}
.blog-more{position:absolute;top:3430px;left:515px;width:170px;text-align:center;padding:12px 0}
.to-top{position:absolute;left:1148px;top:3514px;width:34px;height:34px;background:var(--blue)}

/* footer */
.site-footer{position:absolute;left:0;top:3568px;width:1200px;height:556px;background:var(--black);color:#cfd2d6}
.footer-brand{position:absolute;left:190px;top:48px;text-align:center}
.footer-brand i{display:block;width:56px;height:56px;background:var(--white);margin:0 auto 10px}
.footer-brand span{font-family:"Montserrat",Arial,sans-serif;font-weight:800;font-size:18px;color:var(--white);letter-spacing:2px}
.contact-list{position:absolute;left:420px;top:48px;font-size:11px}
.contact-list li{list-style:none;display:flex;gap:12px;margin-bottom:18px}
.contact-list b{display:block;color:var(--white);font-size:12px}
.footer-links{position:absolute;left:690px;top:48px;font-size:12px;line-height:2}
.footer-links b{color:var(--white);display:block}
.newsletter{position:absolute;left:860px;top:48px;width:220px;font-size:12px;color:var(--white)}
.newsletter .input{margin-top:16px;height:34px;background:var(--white);color:var(--muted);font-size:11px;padding:8px 10px}
.newsletter .btn{margin-top:10px;padding:8px 18px;font-size:11px}
</style>
</head>
<body>

<section class="hero">
  <div class="ph hero-photo" role="img" aria-label="Photo of a cheerful business team celebrating at a laptop in a bright office"></div>
  <div class="hero-copy">
    <div class="eyebrow">For Individuals, Teams and Businesses</div>
    <h1>Discover the Science of Sucess</h1>
    <p>Learn the cutting-edge tools to hack the productivity. It works 100%. Take the active role and experience your growth.</p>
    <a class="btn btn-blue">Take the leap</a>
  </div>
</section>
<div class="dots"><span></span><span></span><span></span></div>

<header class="site-header">
  <div class="brand"><i></i>MENTORVALE</div>
  <div class="topbar"><span>Mail: info@mentorvale.com</span><span>Phone: +1 555 0148 220</span></div>
  <nav class="nav">
    <a>Home</a><a>Coachings</a><a>About Coach</a><a>Blog</a><a>Contact Us</a>
    <svg width="14" height="14" viewBox="0 0 14 14"><circle cx="6" cy="6" r="4.5" fill="none" stroke="#1f2430" stroke-width="1.6"/><line x1="9.3" y1="9.3" x2="13" y2="13" stroke="#1f2430" stroke-width="1.6"/></svg>
    <div class="social"><span></span><span></span><span></span></div>
  </nav>
</header>

<section class="vision">
  <div class="vision-col"><h4>WHY DO I DO THIS</h4><p>Sed ut perspiciatis unde omnis iste natus error sit voluptatem accusantium doloremque laudantium, totam rem aperiam eaque ipsa quae ab illo inventore.</p></div>
  <div class="vision-col"><h4>HOW DO I DO THIS</h4><p>Sed ut perspiciatis unde omnis iste natus error sit voluptatem accusantium doloremque laudantium, totam rem aperiam eaque ipsa quae ab illo inventore.</p></div>
  <div class="vision-col"><h4>WHAT I AM DOING</h4><p>Sed ut perspiciatis unde omnis iste natus error sit voluptatem accusantium doloremque laudantium, totam rem aperiam eaque ipsa quae ab illo inventore.</p></div>
</section>

<div class="coaching-bg"></div>
<div class="coaching-head"><h2>Coaching for Individual, Teams and Business</h2></div>
<p class="coaching-intro">Lorem ipsum dolor sit amet, consectetur adipiscing elit, sed do eiusmod tempor incididunt ut labore et dolore magna aliqua. Ut enim ad minim veniam, quis nostrud exercitation ullamco laboris nisi ut aliquip ex ea commodo consequat. Duis aute irure dolor in reprehenderit in voluptate velit esse cillum dolore eu fugiat nulla pariatur. Excepteur sint occaecat cupidatat non proident, sunt in culpa qui officia deserunt mollit anim id est laborum.</p>

<svg class="arrow" style="left:30px" width="20" height="30" viewBox="0 0 20 30"><polyline points="15,3 4,15 15,27" fill="none" stroke="#9aa0a8" stroke-width="2"/></svg>
<svg class="arrow" style="left:1150px" width="20" height="30" viewBox="0 0 20 30"><polyline points="5,3 16,15 5,27" fill="none" stroke="#9aa0a8" stroke-width="2"/></svg>
<div class="cards">
  <div class="card"><div class="ph" role="img" aria-label="Photo of a coach writing notes during a session" style="background:linear-gradient(180deg,#9aa3ad 0%,#4b525c 60%,#1c2027 100%)"></div><h3>What is Coaching,<br>Why Coaching</h3></div>
  <div class="card"><div class="ph" role="img" aria-label="Photo of colleagues discussing career plans at a table" style="background:linear-gradient(180deg,#c9c0b4 0%,#7c7268 60%,#2a2622 100%)"></div><h3>Career Development</h3></div>
  <div class="card"><div class="ph" role="img" aria-label="Photo of a thoughtful businessman in a dim office" style="background:linear-gradient(180deg,#8d8f94 0%,#4a4c52 60%,#18191c 100%)"></div><h3>Conflicts</h3></div>
</div>

<div class="stats">
  <div class="stat"><b>500+</b><div><h4>Happy Clients</h4><p>Suspendisse facilisis sem sit amet mauris posuere, ut interdum elit aliquet</p></div></div>
  <div class="stat"><b>100%</b><div><h4>Result Oriented</h4><p>Suspendisse facilisis sem sit amet mauris posuere, ut interdum elit aliquet</p></div></div>
  <div class="stat"><b>100%</b><div><h4>Support</h4><p>Suspendisse facilisis sem sit amet mauris posuere, ut interdum elit aliquet</p></div></div>
</div>

<div class="ph about-photo" role="img" aria-label="Portrait photo of the coach in a suit with arms crossed"></div>
<div class="name-card"><h3>JOHN DOE</h3><p>Founder of Mentorvale</p></div>
<section class="about">
  <h2>About the Coach</h2>
  <p>Lorem ipsum dolor sit amet, consectetur adipiscing elit, sed do eiusmod tempor incididunt ut labore et dolore magna aliqua. Ut enim ad minim veniam, quis nostrud exercitation ullamco laboris nisi ut aliquip ex ea commodo consequat.</p>
  <p>Duis aute irure dolor in reprehenderit in voluptate velit esse cillum dolore eu fugiat nulla pariatur. Excepteur sint occaecat cupidatat non proident, sunt in culpa qui officia deserunt mollit anim id est laborum. Sed ut perspiciatis unde omnis iste natus error sit voluptatem accusantium.</p>
  <h3>Want to know more?</h3>
  <p>Fill out the form below and our team will contact you in no time.</p>
  <div class="form">
    <div class="field">Name</div><div class="field">Phone No.</div>
    <div class="field wide">Email ID</div>
    <div class="field wide msg">Your Message</div>
    <span class="btn">Submit</span>
  </div>
</section>

<section class="support">
  <div class="kicker">Sucess Starts with 3 Easy Step</div>
  <h2>Support Concept</h2>
  <p>Lorem ipsum dolor sit amet, consectetur adipiscing elit, sed do eiusmod tempor incididunt ut labore et dolore magna aliqua. Ut enim ad minim veniam, quis nostrud exercitation ullamco laboris nisi ut aliquip ex ea commodo consequat.</p>
  <p>Lorem ipsum dolor sit amet, consectetur adipiscing elit, sed do eiusmod tempor incididunt ut labore et dolore magna aliqua. Ut enim ad minim veniam, quis nostrud exercitation ullamco laboris nisi ut aliquip ex ea commodo consequat.</p>
  <h3>Ready to Start?</h3>
  <p>Lorem ipsum dolor sit amet, consectetur adipiscing elit, sed do eiusmod tempor incididunt ut labore et dolore magna aliqua.</p>
  <span class="btn" style="text-transform:none;padding:10px 20px">Let's Talk</span>
</section>
<div class="timeline"></div>
<div class="step-dot active" style="top:2452px">01</div>
<div class="step-dot" style="top:2628px">02</div>
<div class="step-dot" style="top:2804px">03</div>
<div class="step active" style="top:2400px"><h4>Make a Decision</h4><p>Lorem ipsum dolor sit amet, consectetur adipiscing elit, sed do eiusmod tempor incididunt ut labore et dolore magna aliqua.</p></div>
<div class="step" style="top:2576px"><h4>Schedule a Meeting</h4><p>Lorem ipsum dolor sit amet, consectetur adipiscing elit, sed do eiusmod tempor incididunt ut labore et dolore magna aliqua.</p></div>
<div class="step" style="top:2752px"><h4>Experience Transformation</h4><p>Lorem ipsum dolor sit amet, consectetur adipiscing elit, sed do eiusmod tempor incididunt ut labore et dolore magna aliqua.</p></div>

<h2 class="blog-title">Latest from Blog</h2>
<div class="posts">
  <article class="post"><div class="ph" role="img" aria-label="Photo of people in a meeting room" style="background:linear-gradient(135deg,#6d747d,#2d3138)"></div><h4>Lorem Ipsum Dollar</h4><p>Jun 21, 2020 &nbsp;|&nbsp; by Elmer</p></article>
  <article class="post"><div class="ph" role="img" aria-label="Photo of a desk with a notebook and productivity notes" style="background:linear-gradient(135deg,#e2e2e2,#8f9196)"></div><h4>Lorem Ipsum Dollar</h4><p>Jun 21, 2020 &nbsp;|&nbsp; by Elmer</p></article>
  <article class="post"><div class="ph" role="img" aria-label="Photo of a team workshop in front of a whiteboard" style="background:linear-gradient(135deg,#c8cdd3,#6e7784)"></div><h4>Lorem Ipsum Dollar</h4><p>Jun 21, 2020 &nbsp;|&nbsp; by Elmer</p></article>
</div>
<span class="btn blog-more">Explore More</span>
<div class="to-top"><svg width="34" height="34" viewBox="0 0 34 34"><polyline points="11,20 17,14 23,20" fill="none" stroke="#fff" stroke-width="2"/></svg></div>

<footer class="site-footer">
  <div class="footer-brand"><i></i><span>MENTORVALE</span></div>
  <ul class="contact-list">
    <li><svg width="16" height="16" viewBox="0 0 16 16"><rect x="1" y="3" width="14" height="10" fill="none" stroke="#fff" stroke-width="1.4"/><polyline points="1,3 8,9 15,3" fill="none" stroke="#fff" stroke-width="1.4"/></svg><div><b>Email</b>info@mentorvale.com</div></li>
    <li><svg width="16" height="16" viewBox="0 0 16 16"><path d="M3 1h3l1.5 4-2 1.2a9 9 0 0 0 4.3 4.3L11 8.5l4 1.5v3a2 2 0 0 1-2 2A12 12 0 0 1 1 3a2 2 0 0 1 2-2z" fill="#fff"/></svg><div><b>Phone</b>+1 555 0148 220</div></li>
    <li><svg width="16" height="16" viewBox="0 0 16 16"><path d="M8 1a5 5 0 0 1 5 5c0 4-5 9-5 9S3 10 3 6a5 5 0 0 1 5-5z" fill="#fff"/><circle cx="8" cy="6" r="1.8" fill="#0b0b0c"/></svg><div><b>Address</b>24 Linden Row, Brookfield</div></li>
  </ul>
  <div class="footer-links"><b>About Us</b>Coaching<br>Help<br>Contact<br>Disclaimer</div>
  <div class="newsletter">Subscribe to get the latest content by Mentorvale straight in your inbox.
    <div class="input">Enter Email</div>
    <span class="btn">Subscribe</span>
  </div>
</footer>

</body>
</html>
```